Revamp business card for upcoming new practice

We need a business card with our new practice location details. We are a boutique dental practice. Our new practice design is timeless black, white and grey colour scheme with a pop of our purple.
We are moving away from the amount of purple on website and overall practice.
Simple, elegant, clean and eye catching.

Industry/Entity Type

Dental Clinic

Contact Information for Business Card

See Design brief attached

Font styles to use
Serif
Sans Serif

Requirements
Must have
• New design | Front requirements:
• • Business logo (see attached files)
• • Address: 417 Larkfield Road Larkfield Vic 3188
• • Phone number: 03 9684 2719
• • Email: info@orvellodental.example.au
• • Website address: orvellodental.example.au
• New design | Back requirements:
• • Dentist Details: Dr. Leon Fairbrook & Associates
• B.D.S Brightwell College Norfield
• Grad. Dip. Clin. Dent. (Conscious Sedation & Pain Control). University of Carrowby.
• • Your Next Appointment is: OR no text and just lines for writing an appointment
• • Lines for writing the appointment minimum 2, maximum 3.
• • Cancellation Policy: We require a minimum of 48 hours or a fee will apply
Nice to have
• Black, grey and white colours with the touch of purple
Should not have
• Icon/images for contact details
• Be entirely purple.

```html
<!DOCTYPE html>
<html lang="en">
<head>
<meta charset="utf-8">
<title>Orvello Dental – Business Card</title>
<link href="https://fonts.googleapis.com/css2?family=Arimo:wght@400;700&display=swap" rel="stylesheet">
<style>
  :root {
    --purple: #8e45a8;
    --purple-light: #a564bd;
    --ink: #1f1f1f;
    --grey: #b9b9b9;
    --black-panel: #2b2b2b;
    --card: #ffffff;
    --backdrop: #e9e9ea;
  }
  * { box-sizing: border-box; margin: 0; padding: 0; }
  html, body { width: 1200px; height: 660px; overflow: hidden; }
  body {
    background: var(--backdrop);
    font-family: "Arimo", Arial, sans-serif;
    color: var(--ink);
    position: relative;
  }
  .card {
    position: absolute;
    top: 175px;
    width: 540px;
    height: 310px;
    background: var(--card);
    overflow: hidden;
    box-shadow: 0 6px 18px rgba(0,0,0,.18);
  }
  .card--front { left: 40px; }
  .card--back { left: 620px; }
  .card svg.shapes { position: absolute; inset: 0; }

  /* Front */
  .brand {
    position: absolute; left: 30px; top: 34px;
    display: flex; align-items: center; gap: 12px;
  }
  .brand__mark { width: 22px; height: 22px; background: var(--purple); }
  .brand__name {
    font-size: 34px; font-weight: 400; letter-spacing: 1px;
    color: var(--ink); text-transform: lowercase;
  }
  .contact {
    position: absolute; left: 30px; top: 150px;
    font-size: 17px; line-height: 21px; color: var(--ink);
  }
  .contact__address { margin-top: 8px; }

  /* Back */
  .dentist {
    position: absolute; left: 26px; top: 70px; width: 255px;
    font-weight: 700; line-height: 1;
  }
  .dentist__name { font-size: 20px; letter-spacing: .2px; white-space: nowrap; }
  .dentist__assoc { font-size: 15px; margin-top: 4px; }
  .qualifications {
    position: absolute; left: 292px; top: 14px; width: 240px;
    color: #fff; font-size: 10px; line-height: 14px;
  }
  .qualifications strong { font-size: 11px; }
  .policy {
    position: absolute; left: 40px; top: 212px; width: 200px;
    color: #fff; font-size: 11.5px; line-height: 15px;
  }
  .policy__title { text-transform: uppercase; margin-bottom: 8px; }
  .appointment {
    position: absolute; left: 300px; top: 118px; width: 215px;
  }
  .appointment__label { font-size: 12px; font-weight: 700; margin-bottom: 26px; }
  .appointment__line {
    border-bottom: 2px dotted var(--ink);
    height: 34px;
  }
</style>
</head>
<body>

<section class="card card--front" aria-label="Card front">
  <svg class="shapes" width="540" height="310" viewBox="0 0 540 310" aria-hidden="true">
    <defs>
      <linearGradient id="frontWedge" x1="0" y1="0" x2="1" y2="1">
        <stop offset="0" stop-color="#9a52b4"/>
        <stop offset="1" stop-color="#7d3996"/>
      </linearGradient>
    </defs>
    <polygon points="250,88 540,88 540,205 420,205" fill="url(#frontWedge)"/>
    <rect x="20" y="88" width="230" height="6" fill="var(--grey)"/>
  </svg>
  <div class="brand">
    <span class="brand__mark"></span>
    <span class="brand__name">Orvello Dental</span>
  </div>
  <div class="contact">
    <p>03 9684 2719</p>
    <p>info@orvellodental.example.au</p>
    <p>orvellodental.example.au</p>
    <p class="contact__address">417 Larkfield Road<br>Larkfield Vic 3188</p>
  </div>
</section>

<section class="card card--back" aria-label="Card back">
  <svg class="shapes" width="540" height="310" viewBox="0 0 540 310" aria-hidden="true">
    <defs>
      <linearGradient id="panel" x1="0" y1="0" x2="1" y2="1">
        <stop offset="0" stop-color="#3a3a3a"/>
        <stop offset="1" stop-color="#141414"/>
      </linearGradient>
      <linearGradient id="backWedge" x1="0" y1="0" x2="1" y2="1">
        <stop offset="0" stop-color="#9a52b4"/>
        <stop offset="1" stop-color="#7d3996"/>
      </linearGradient>
    </defs>
    <polygon points="282,0 540,0 540,100 270,100" fill="url(#panel)"/>
    <polygon points="22,178 270,100 255,295 22,295" fill="url(#backWedge)"/>
  </svg>

  <div class="qualifications">
    <p><strong>B.D.S</strong> Brightwell College Norfield</p>
    <p><strong>Grad. Dip. Clin. Dent.</strong></p>
    <p>(Conscious Sedation &amp; Pain Control).</p>
    <p>University of Carrowby.</p>
  </div>

  <div class="dentist">
    <p class="dentist__name">DR. LEON FAIRBROOK</p>
    <p class="dentist__assoc">&amp; Associates</p>
  </div>

  <div class="policy">
    <p class="policy__title">Cancellation policy:</p>
    <p>We require a minimum of 48 hours or a fee will apply</p>
  </div>

  <div class="appointment">
    <p class="appointment__label">Your Next Appointment is:</p>
    <div class="appointment__line"></div>
    <div class="appointment__line"></div>
    <div class="appointment__line"></div>
  </div>
</section>

</body>
</html>
```